Australia-Wide Industry Leader Bookkeeping Business Website Design Required

We need a website designed for our 10 year old bookkeeping business, Barwick & Lund. Barwick & Lund has been servicing the local & interstate communities of Australia, providing first-class BAS & Bookkeeping services with a personal touch unmatched by anyone else in the county.

What began 10 years ago as a small business focusing on family, friends and the local community, it has since grown into a well respected business with 95% of their business based solely on word of mouth and personal referrals from around Australia.

We would like to see designs that incorporate our existing brand/logo. The colours to be used on the website should be colours that work well with our logo. The design should communicate maturity, trust and confidence with a Web 2.0 look and feel.

We have produced mockups of the entire website as well as assets used in the mockups. Please reference the attached files. The mockups are an example of all the design elements that we want on each page. Designers are encouraged to use the mockups as a guideline only and for designers to use their own creativity.
Updates

This message is for new graphic designers who are considering commencing work on this project. Thank you for expressing an interest in our project. We would like to inform you that this project is close to completion as we have a number designs under very serious consideration.

We are currently in a position where we are disinterested providing feedback to improve on new designs submitted. We will provide feedback to improve new designs only if the submitted designs are very close to what we want for our website, and will only require 1 or 2 revision rounds to refine before the project completion date we will not work with designers to refine their newly submitted designs.

We feel that it is important for all designers to know the above information as we feel that your time and effort may be better spent working on another project.

Thank you for your understanding.

A big thank you for all the designs submitted. We are now in the process of selecting a design. Please be patient during this process. Thank you.

Target Market(s)

Busy Business Owners

Industry/Entity Type

Small Business

Requirements
Must have
• We require a rectangular "slide show" type feature to serve as a "teaser" to arouse the emotions of our website visitors. Each slide asks a specific question. The questions are:

- Is your paperwork in a mess?
- Do you need to get organised for the end of financial year?
- Are you sick & tired of endless amounts of paperwork & BASs?
- Do you feel frustrated & annoyed because you know your books need to be done?
- Do you lack the time & patience to get your paperwork done?
- Do you wish you had more time to do the things you enjoy doing?
- Contact Barwick & Lund today and we will transform your chaos into order.

Underneath the slide show will be a button to "Call Barwick & Lund Now - 03 5550 1827".

```html
<!DOCTYPE html>
<html lang="en">
<head>
<meta charset="utf-8">
<title>Barwick &amp; Lund — Bookkeeping</title>
<link href="https://fonts.googleapis.com/css2?family=Gelasio:ital,wght@0,400;0,700;1,400;1,700&family=Sorts+Mill+Goudy&family=Open+Sans:wght@400;600&display=swap" rel="stylesheet">
<style>
:root{
  --bg:#f2f2f2;
  --red:#8b0a0a;
  --ink:#222;
  --text:#555;
  --muted:#777;
  --rule:#d9d9d9;
  --tick:#2f8a6a;
  --blue:#1ea0dc;
  --white:#fff;
  --badge:#cfcfcf;
}
*{box-sizing:border-box;margin:0;padding:0}
html,body{width:875px;height:1200px;overflow:hidden}
body{background:var(--bg);font-family:'Gelasio',Georgia,serif;color:var(--text);position:relative}
.abs{position:absolute}

.logo{left:310px;top:11px;width:256px;height:45px;border:1px solid #333;background:var(--white);display:flex;align-items:center;justify-content:center;gap:8px}
.logo-mark{width:14px;height:14px;background:var(--red)}
.logo-name{font-weight:700;font-size:22px;color:var(--red)}

.nav{left:146px;top:78px;width:583px;height:30px;background:linear-gradient(#fff,#f1f1f1);border:1px solid #e2e2e2;border-bottom:2px solid var(--red);border-radius:4px;display:flex;align-items:center;padding-left:15px}
.nav a{font-size:10px;color:#444;text-decoration:none;letter-spacing:.5px;padding:2px 7px;margin-right:8px}
.nav a.active{background:var(--red);color:var(--white);border-radius:3px;padding:1px 8px}

.quote{left:146px;top:118px;width:583px;height:56px;background:var(--white);border:1px solid #e2e2e2;border-radius:3px;padding:5px 10px;font-style:italic;font-size:8.4px;line-height:15.3px;color:var(--muted)}
.quote b{font-style:normal;font-size:15px;color:#888;line-height:0;vertical-align:-3px}

.hero{left:146px;top:187px;width:583px;height:160px;border:1px solid #d6d6d6;background:linear-gradient(#fafafa,#e9e9e9);overflow:hidden}
.hero-photo{left:0;top:0;width:250px;height:160px;background:linear-gradient(135deg,#d9d9d9,#c4a6a8 55%,#8d8d8d)}
.hero-title{left:250px;top:26px;width:333px;text-align:center;font-style:italic;font-weight:700;font-size:14.5px;line-height:22px;color:#333}
.hero-shadow{left:325px;top:88px;width:160px;height:10px;border-radius:50%;background:radial-gradient(ellipse,rgba(0,0,0,.35),rgba(0,0,0,0) 70%)}
.hero-bar{left:0;top:120px;width:583px;height:40px;background:rgba(110,110,110,.92)}
.hero-question{left:292px;top:131px;font-size:14px;color:var(--white);display:flex;align-items:center;gap:9px}
.play{width:0;height:0;border-left:9px solid var(--blue);border-top:5px solid transparent;border-bottom:5px solid transparent}

.heading{font-family:'Sorts Mill Goudy',Georgia,serif;font-weight:400;font-size:14px;color:var(--ink);display:flex;gap:7px;align-items:flex-start;padding-bottom:8px;border-bottom:1px solid var(--rule);line-height:17.5px}
.heading svg{flex:none;margin-top:4px}
.body-copy{font-style:italic;font-size:8.4px;line-height:15.3px;color:var(--muted)}

.ticks{list-style:none}
.ticks li{position:relative;padding-left:16px;font-style:italic;font-size:8.2px;color:#555;height:18px;line-height:16px;border-bottom:1px dotted #bbb}
.ticks li::before{content:"";position:absolute;left:0;top:3px;width:8px;height:8px;border:1px solid var(--tick);background:var(--white)}
.ticks li::after{content:"";position:absolute;left:3px;top:4px;width:2px;height:4px;border:solid var(--tick);border-width:0 1.5px 1.5px 0;transform:rotate(45deg)}
.ticks li.tall{height:36px;line-height:15px;padding-top:1px;border-bottom:none}

.sub{list-style:none}
.sub li{position:relative;padding-left:10px;font-style:italic;font-size:8.2px;color:#555;height:18px;line-height:16px}
.sub li::before{content:"";position:absolute;left:0;top:5px;border-left:5px solid var(--blue);border-top:3px solid transparent;border-bottom:3px solid transparent}

.call{left:484px;top:480px;width:245px;height:50px}
.call-top{height:25px;background:linear-gradient(#fff,#dcdcdc);font-family:'Open Sans',Arial,sans-serif;font-size:15.5px;color:#444;padding-left:38px;line-height:25px}
.call-num{height:25px;background:var(--red);font-family:'Open Sans',Arial,sans-serif;font-size:16px;color:var(--white);padding-left:40px;line-height:25px;letter-spacing:.5px}
.call-photo{left:672px;top:462px;width:57px;height:68px;background:linear-gradient(#e9d2c0,#f4f4f4)}

.map{left:485px;top:633px;width:244px;height:188px;border:1px solid #ddd;background:linear-gradient(#f4f4f4,#dcdcdc)}

.partner{position:absolute;top:1064px;height:70px;background:var(--badge);border-radius:3px}

.footer{left:0;top:1156px;width:875px;height:44px;border-top:2px solid var(--red);background:linear-gradient(#fafafa,#e3e3e3)}
.follow{left:146px;top:1166px;font-style:italic;font-weight:700;font-size:7.5px;color:#333;display:flex;align-items:center;gap:5px}
.social{width:9px;height:9px;border-radius:2px;background:#8a8a8a}
.copyright{right:146px;top:1166px;font-style:italic;font-size:7.5px;color:#333}
.modified{right:146px;top:1182px;font-style:italic;font-size:6.5px;color:#888}
</style>
</head>
<body>

<div class="abs logo"><span class="logo-mark"></span><span class="logo-name">Barwick &amp; Lund</span></div>

<nav class="abs nav">
  <a class="active" href="#">Home</a><a href="#">About Us</a><a href="#">Services</a><a href="#">Testimonials</a><a href="#">Articles</a><a href="#">Endorsements</a><a href="#">Links</a><a href="#">Contact Us</a>
</nav>

<div class="abs quote"><b>“</b> Lorem Ipsum is simply dummy text of the printing and typesetting industry. Lorem Ipsum has been the industry's standard dummy text ever since the 1500s, when an unknown printer took a galley of type and scrambled it to make a type specimen book. Lorem Ipsum is simply dummy text of the printing type specimen book. <b>”</b></div>

<section class="abs hero">
  <div class="abs hero-photo" role="img" aria-label="Photo of a frustrated office worker at a computer"></div>
  <p class="abs hero-title">Lorem Ipsum is simply dummy text<br>of the printing and industry.</p>
  <div class="abs hero-shadow"></div>
  <div class="abs hero-bar"></div>
  <p class="abs hero-question"><span class="play"></span>Is your paperwork in a mess?</p>
</section>

<svg width="0" height="0" style="position:absolute">
  <symbol id="arrow" viewBox="0 0 12 9"><path d="M0 3h6V0l6 4.5L6 9V6H0z" fill="#8b0a0a"/></symbol>
</svg>

<h2 class="abs heading" style="left:146px;top:366px;width:278px"><svg width="11" height="8"><use href="#arrow"/></svg>Welcome to Barwick &amp; Lund</h2>
<p class="abs body-copy" style="left:146px;top:398px;width:560px">Lorem Ipsum is simply dummy text of the printing and typesetting industry. Lorem Ipsum has been the industry's standard dummy text ever since the 1500s, when an unknown printer took a galley of type and scrambled it to make a type specimen book.Lorem Ipsum is simply dummy text of the printing and typesetting industry. Lorem Ipsum has been the industry's standard dummy text ever since the 1500s, when an unknown printer took a galley of type and scrambled it to make a type specimen book.</p>

<h2 class="abs heading" style="left:146px;top:479px;width:278px"><svg width="11" height="8"><use href="#arrow"/></svg>To Summarise</h2>
<ul class="abs ticks" style="left:146px;top:512px;width:113px">
  <li>Lorem Ipsum is simply</li><li>Lorem Ipsum is simply</li><li>Lorem Ipsum is simply</li><li>Lorem Ipsum is simply</li><li>Lorem Ipsum is simply</li><li>Lorem Ipsum is simply</li>
</ul>
<ul class="abs ticks" style="left:316px;top:512px;width:113px">
  <li>Lorem Ipsum is simply</li><li>Lorem Ipsum is simply</li><li>Lorem Ipsum is simply</li><li>Lorem Ipsum is simply</li><li>Lorem Ipsum is simply</li><li>Lorem Ipsum is simply</li>
</ul>

<h2 class="abs heading" style="left:146px;top:643px;width:278px"><svg width="11" height="8"><use href="#arrow"/></svg>What makes Barwick &amp; Lund different<br>from other Bookkeepers</h2>
<ul class="abs ticks" style="left:146px;top:692px;width:221px">
  <li>Lorem Ipsum is simply dummy text of the printing.</li>
  <li>Lorem Ipsum is simply.</li>
  <li>Lorem Ipsum is simply dummy text of the printing.</li>
  <li>Lorem Ipsum is simply dummy text of the printing.</li>
  <li>Lorem Ipsum is simply dummy.</li>
  <li class="tall">Lorem Ipsum is simply dummy text of the printing and typesetting industry. Lorem Ipsum has been.</li>
</ul>
<ul class="abs sub" style="left:171px;top:825px">
  <li>Lorem Ipsum is simply</li><li>Lorem Ipsum is simply dummy text of the printing.</li><li>Lorem Ipsum is simply</li><li>Lorem Ipsum is simply dummy text.</li>
</ul>
<p class="abs body-copy" style="left:162px;top:904px;width:220px;color:#555">Lorem Ipsum is simply dummy text of the printing and typesetting industry.</p>
<ul class="abs sub" style="left:171px;top:941px">
  <li>Lorem Ipsum is simply dummy text of the.</li><li>Lorem Ipsum is simply</li><li>Lorem Ipsum is simply dummy text of the printing.</li><li>Lorem Ipsum is simply</li>
</ul>
<p class="abs body-copy" style="left:162px;top:1023px;font-weight:700;color:#333">Lorem Ipsum is simply dummy text of the printing and industry.</p>

<div class="abs call-photo" role="img" aria-label="Photo of a customer service agent with headset"></div>
<div class="abs call">
  <div class="call-top">CALL US NOW!</div>
  <div class="call-num">03 5550 1827</div>
</div>

<h2 class="abs heading" style="left:484px;top:544px;width:278px"><svg width="11" height="8"><use href="#arrow"/></svg>To Summarise</h2>
<p class="abs body-copy" style="left:485px;top:575px;width:245px">Lorem Ipsum is simply dummy text of the printing and typesetting industry. Lorem Ipsum has been the industry's standard dummy text ever since the 1500s.</p>

<div class="abs map" role="img" aria-label="Map of Australia marking the major cities served"></div>

<p class="abs body-copy" style="left:484px;top:836px;font-weight:700;color:#333">Qualifications, Memberships and Partnerships</p>
<ul class="abs ticks" style="left:484px;top:862px;width:221px">
  <li>Lorem Ipsum is simply dummy text of the printing.</li>
  <li>Lorem Ipsum is simply.</li>
  <li>Lorem Ipsum is simply dummy text of the printing.</li>
  <li>Lorem Ipsum is simply dummy text of the printing.</li>
  <li>Lorem Ipsum is simply dummy.</li>
  <li>Lorem Ipsum is simply dummy text of the printing.</li>
  <li>Lorem Ipsum is simply dummy.</li>
</ul>

<div class="partner" style="left:146px;width:46px" role="img" aria-label="Partner badge"></div>
<div class="partner" style="left:241px;width:68px" role="img" aria-label="Membership badge"></div>
<div class="partner" style="left:358px;width:84px" role="img" aria-label="Network badge"></div>
<div class="partner" style="left:498px;width:38px" role="img" aria-label="Partner badge"></div>
<div class="partner" style="left:585px;width:145px;top:1082px;height:28px" role="img" aria-label="Government partner badge"></div>

<footer class="abs footer"></footer>
<div class="abs follow">Follow Us on: <span class="social"></span><span class="social"></span></div>
<p class="abs copyright">The contents of this site are copyright © 2012, Barwick &amp; Lund. All Rights Reserved.</p>
<p class="abs modified">This page was last modified sat 25 Jun 2011</p>

</body>
</html>
```